Business cards for law firm with global theme

I'd like business cards with contact info for two offices. They should include the colors and font of the new logo design, which is a stylized globe with an "F" in it. The feel should be very modern and professional.

```html
<!DOCTYPE html>
<html lang="en">
<head>
<meta charset="utf-8">
<title>Marvello Law — Business Cards</title>
<link href="https://fonts.googleapis.com/css2?family=Lato:wght@400;700&family=Roboto:wght@300;400&display=swap" rel="stylesheet">
<style>
  :root {
    --navy: #163d6b;
    --sky: #22a9e1;
    --white: #ffffff;
    --backdrop: #2a2a2a;
    --text-contact: #1f3d66;
  }
  * { box-sizing: border-box; margin: 0; padding: 0; }
  html, body {
    width: 1200px; height: 1200px; overflow: hidden;
    background: var(--backdrop);
  }
  .canvas { position: relative; width: 1200px; height: 1200px; }

  .card {
    position: absolute; left: 239px; width: 722px; height: 412px;
    border-radius: 18px; overflow: hidden;
    box-shadow: 0 10px 24px rgba(0,0,0,0.45);
  }
  .card--front { top: 140px; background: var(--white); }
  .card--back { top: 645px; }

  .front-shape { position: absolute; inset: 0; width: 722px; height: 412px; }

  .front-mark {
    position: absolute; left: 44px; top: 41px;
    width: 118px; height: 118px; border-radius: 50%;
    background: var(--white);
  }

  .firm-name {
    position: absolute; right: 39px; top: 48px;
    font-family: "Lato", sans-serif; font-weight: 700;
    font-size: 46px; letter-spacing: 0.5px; line-height: 1;
    color: var(--navy); white-space: nowrap;
  }

  .person { position: absolute; right: 39px; top: 196px; text-align: right; }
  .person__name {
    font-family: "Lato", sans-serif; font-weight: 700;
    font-size: 31px; color: var(--navy); line-height: 1.1;
  }
  .person__title {
    font-family: "Lato", sans-serif; font-weight: 400;
    font-size: 21px; color: var(--sky); line-height: 1.2;
  }

  .contacts {
    position: absolute; right: 39px; top: 271px;
    list-style: none; display: flex; flex-direction: column; gap: 12px;
  }
  .contact {
    display: flex; align-items: center; justify-content: flex-end; gap: 11px;
    font-family: "Roboto", sans-serif; font-weight: 300;
    font-size: 19px; color: var(--text-contact); height: 25px;
  }
  .contact__icon { width: 25px; height: 25px; flex: none; }

  .back-field {
    position: absolute; inset: 0;
    background:
      linear-gradient(167deg, var(--sky) 0%, var(--sky) 42%, var(--navy) 58%, var(--navy) 100%);
  }
  .back-brand {
    position: absolute; left: 546px; top: 209px;
    transform: translateX(-50%);
    display: flex; flex-direction: column; align-items: center; gap: 22px;
  }
  .back-brand__mark {
    width: 86px; height: 86px; border-radius: 50%; background: var(--white);
  }
  .back-brand__name {
    font-family: "Lato", sans-serif; font-weight: 700;
    font-size: 36px; letter-spacing: 0.5px; line-height: 1;
    color: var(--white); white-space: nowrap;
  }
</style>
</head>
<body>
<main class="canvas">

  <section class="card card--front" aria-label="Business card front">
    <svg class="front-shape" viewBox="0 0 722 412" aria-hidden="true">
      <path d="M0 0 H312 C212 118 166 262 161 412 H0 Z" fill="var(--sky)"/>
      <path d="M0 0 H298 C200 118 154 262 149 412 H0 Z" fill="var(--navy)"/>
    </svg>
    <div class="front-mark" aria-hidden="true"></div>

    <h1 class="firm-name">MARVELLO LAW</h1>

    <div class="person">
      <p class="person__name">Your Name Here</p>
      <p class="person__title">Designation</p>
    </div>

    <ul class="contacts">
      <li class="contact">
        <span>123 NW Somewhere St., Somewhere City</span>
        <svg class="contact__icon" viewBox="0 0 24 24" aria-hidden="true">
          <circle cx="12" cy="12" r="11" fill="none" stroke="var(--navy)" stroke-width="1.6"/>
          <path d="M12 5.5a4 4 0 0 0-4 4c0 3 4 8 4 8s4-5 4-8a4 4 0 0 0-4-4z" fill="var(--navy)"/>
          <circle cx="12" cy="9.5" r="1.5" fill="var(--white)"/>
        </svg>
      </li>
      <li class="contact">
        <span>youre@email.com</span>
        <svg class="contact__icon" viewBox="0 0 24 24" aria-hidden="true">
          <circle cx="12" cy="12" r="11" fill="none" stroke="var(--navy)" stroke-width="1.6"/>
          <rect x="6" y="8" width="12" height="8.5" rx="1.2" fill="var(--navy)"/>
          <path d="M6.5 8.8 12 12.8 17.5 8.8" fill="none" stroke="var(--white)" stroke-width="1.2"/>
        </svg>
      </li>
      <li class="contact">
        <span>(000) 123-4567</span>
        <svg class="contact__icon" viewBox="0 0 24 24" aria-hidden="true">
          <circle cx="12" cy="12" r="11" fill="none" stroke="var(--navy)" stroke-width="1.6"/>
          <path d="M9 6.5l1.6 2.8-1.2 1.3c.7 1.6 1.8 2.8 3.4 3.6l1.3-1.2 2.7 1.6-.8 2.2c-4.4-.4-8-4.2-8.2-8.6z" fill="none" stroke="var(--navy)" stroke-width="1.5" stroke-linejoin="round"/>
        </svg>
      </li>
    </ul>
  </section>

  <section class="card card--back" aria-label="Business card back">
    <div class="back-field" role="img" aria-label="Large globe-arc brand decoration in sky blue and navy"></div>
    <div class="back-brand">
      <div class="back-brand__mark" aria-hidden="true"></div>
      <p class="back-brand__name">MARVELLO LAW</p>
    </div>
  </section>

</main>
</body>
</html>
```